Podcast cover design for a new podcast called 'Island Bright Voices'

I would like a clean, professional and impactful design for a new podcast I am launching called 'Island Bright Voices'. 'Island Bright Voices,' is a podcast featuring conversations with the island's groundbreaking entrepreneurs, technologists, artists, and scientists. Each episode uncovers the stories and insights of visionaries who are shaping Taiwan's future through cutting-edge startups, technological breakthroughs, artistic innovation, and scientific discovery. The podcast cover needs to look professional and be impactful. Ideally, I would also like the podcast cover to feature an photo or image of myself. Please see uploaded two recent photos of myself which you can crop etc for the podcast cover.

```html
<!DOCTYPE html>
<html lang="en">
<head>
<meta charset="utf-8">
<title>Island Bright Voices – Podcast Cover</title>
<link href="https://fonts.googleapis.com/css2?family=Archivo:wght@400;800&display=swap" rel="stylesheet">
<style>
  :root {
    --backdrop: #d99cfb;
    --cover-top: #4d1176;
    --cover-mid: #3a0f5c;
    --cover-bottom: #1e0a2a;
    --highlight: #5a1d8a;
    --title: #ffffff;
    --subtitle: #d79cf7;
    --glow: #a64ee6;
  }
  html, body {
    margin: 0;
    width: 1200px;
    height: 1200px;
    overflow: hidden;
    background: var(--backdrop);
  }
  .cover {
    position: absolute;
    left: 245px;
    top: 245px;
    width: 710px;
    height: 710px;
    overflow: hidden;
    background: linear-gradient(180deg, var(--cover-top) 0%, var(--cover-mid) 45%, var(--cover-bottom) 100%);
    font-family: "Archivo", Arial, sans-serif;
  }
  .cover__glow {
    position: absolute;
    left: 480px;
    top: 560px;
    width: 320px;
    height: 260px;
    border-radius: 50%;
    background: radial-gradient(closest-side, rgba(166, 78, 230, 0.85), rgba(166, 78, 230, 0));
  }
  .cover__mic {
    position: absolute;
    left: -20px;
    top: 560px;
    width: 170px;
    height: 170px;
    border-radius: 50%;
    background: radial-gradient(closest-side, rgba(90, 25, 140, 0.9), rgba(90, 25, 140, 0));
  }
  .cover__host {
    position: absolute;
    left: 286px;
    top: 56px;
    width: 424px;
    height: 654px;
    border-radius: 200px 200px 0 0;
    background: linear-gradient(180deg, #6b6b6b 0%, #d8d8d8 35%, #bfa6d0 70%, #9a62c6 100%);
  }
  .title {
    position: absolute;
    left: 40px;
    top: 204px;
    margin: 0;
    color: var(--title);
    font-weight: 800;
    font-size: 52px;
    line-height: 50px;
    letter-spacing: 0.5px;
    text-transform: uppercase;
  }
  .title__line { display: block; }
  .title__line--highlight {
    display: inline-block;
    background: var(--highlight);
    border-radius: 6px;
    padding: 6px 10px 4px 6px;
    margin-left: -6px;
    margin-bottom: 4px;
    box-shadow: 0 2px 6px rgba(0, 0, 0, 0.35);
  }
  .subtitle {
    position: absolute;
    left: 42px;
    top: 374px;
    margin: 0;
    color: var(--subtitle);
    font-weight: 400;
    font-size: 16px;
    line-height: 23px;
    text-transform: uppercase;
  }
</style>
</head>
<body>
  <main class="cover">
    <div class="cover__glow"></div>
    <div class="cover__mic" role="img" aria-label="Blurred studio microphone"></div>
    <div class="cover__host" role="img" aria-label="Black and white portrait of the podcast host in a dark blazer and white shirt"></div>
    <h1 class="title">
      <span class="title__line title__line--highlight">Island</span>
      <span class="title__line">Bright</span>
      <span class="title__line">Voices</span>
    </h1>
    <p class="subtitle">Conversations with<br>Taiwan’s visionaries</p>
  </main>
</body>
</html>
```